Zielgruppe
Seminare, Vorträge , Therapien, Beratung, Coaching
WEchseljahre Beratung
Sexualtherapie, Sexualberatung
Mentaltraining
Es soll Frauen gefallen und ermuntern zum Seminar zu kommen, frü Thema Wechseljahre interessieren
Aufgabenstellung
Grösse A5 Hochkant

```html
<!DOCTYPE html>
<html lang="de">
<head>
<meta charset="utf-8">
<title>Wechseljahre – Vol. 2</title>
<link href="https://fonts.googleapis.com/css2?family=Bebas+Neue&family=Oswald:wght@300&family=Merriweather:ital,wght@1,400&family=Merriweather+Sans:wght@800&family=Open+Sans:wght@400;600;700&display=swap" rel="stylesheet">
<style>
  :root{
    --blue:#00a9d1;
    --blue-light:#5cc3dd;
    --yellow:#f7ea3c;
    --ink:#333333;
    --white:#ffffff;
  }
  *{box-sizing:border-box;margin:0;padding:0}
  html,body{width:865px;height:1200px;overflow:hidden;background:var(--white)}
  .flyer{position:relative;width:865px;height:1200px;background:var(--white);font-family:"Open Sans",sans-serif}
  .abs{position:absolute}
  .title{left:76px;top:48px;font-family:"Bebas Neue",sans-serif;font-weight:400;font-size:110px;line-height:1;color:var(--blue);letter-spacing:1.5px;white-space:nowrap}
  .vol-badge{left:691px;top:24px;width:122px;height:122px}
  .subtitle{left:76px;top:143px;font-family:"Bebas Neue",sans-serif;font-weight:400;font-size:47px;line-height:1;color:var(--blue);white-space:nowrap}
  .hero-photo{left:22px;top:184px;width:420px;height:514px;
    background:radial-gradient(ellipse at 50% 38%,#e9d3c4 0%,#c9dfe6 28%,#2b3140 56%,#ffffff 78%)}
  .tagline{left:458px;top:228px;width:360px;text-align:center;font-family:"Merriweather",serif;font-weight:400;font-style:italic;font-size:28px;line-height:36px;color:var(--ink)}
  .intro{left:468px;top:362px;width:340px;text-align:center;font-size:16.5px;line-height:26px;color:var(--blue)}
  .date{left:438px;top:532px;width:400px;text-align:center;font-family:"Bebas Neue",sans-serif;font-size:82px;line-height:1;color:var(--blue)}
  .meta{left:418px;width:440px;text-align:center;font-family:"Bebas Neue",sans-serif;color:var(--blue);white-space:nowrap;line-height:1}
  .meta .light{font-family:"Oswald",sans-serif;font-weight:300;text-transform:uppercase}
  .meta-time{top:605px;font-size:40px}
  .meta-time .light{font-size:23px}
  .meta-time .small{font-size:28px}
  .meta-place{top:650px;font-size:29px}
  .meta-place .light{font-size:21px}
  .band{left:0;top:698px;width:865px;height:381px;background:var(--blue)}
  .band-heading{font-family:"Merriweather Sans",sans-serif;font-weight:800;color:var(--yellow);font-size:22.5px;line-height:1;left:95px;white-space:nowrap}
  .h-change{top:729px}
  .h-questions{top:891px}
  .body-col{top:758px;width:328px;color:var(--white);font-size:13.4px;line-height:20px}
  .body-col span{display:block;text-align:justify;text-align-last:justify;white-space:nowrap}
  .body-col span.last{text-align-last:left}
  .col-left{left:95px}
  .col-right{left:445px}
  .questions{top:924px;width:340px;list-style:none;color:var(--white);font-size:12.8px;font-weight:600;line-height:18px}
  .q-left{left:95px}
  .q-right{left:446px}
  .questions li{position:relative;padding-left:16px;margin-bottom:5px;white-space:nowrap}
  .questions li::before{content:"";position:absolute;left:0;top:5px;width:8px;height:8px;background:var(--white)}
  .portrait{left:63px;top:1037px;width:116px;height:116px;border-radius:50%;border:4px solid var(--white);
    background:radial-gradient(circle at 50% 45%,#e3c2b0 0%,#d7a99a 35%,#9bb7d0 70%,#f1f1f1 100%)}
  .brand-mark{left:686px;top:1035px;width:116px;height:116px;border-radius:50%;border:4px solid var(--white);background:var(--blue-light);display:flex;align-items:center;justify-content:center;color:var(--white);font-weight:700;font-size:17px}
  .contact{left:198px;top:1086px;width:468px;text-align:center}
  .contact-title{font-size:19px;font-weight:700;color:var(--blue);line-height:24px}
  .contact-line{font-size:12.6px;font-weight:700;color:var(--blue);line-height:19px}
  .contact-name{font-size:12.6px;font-weight:700;color:var(--ink);line-height:18px;margin-top:4px}
  .contact-role{font-size:12.6px;color:var(--ink);line-height:18px}
  .contact-web{font-size:12.6px;font-weight:700;color:var(--blue);line-height:18px}
  .footer-bar{left:360px;top:1193px;width:146px;height:7px;background:var(--blue)}
</style>
</head>
<body>
<div class="flyer">
  <h1 class="abs title">WECHSELJAHRE —</h1>
  <svg class="abs vol-badge" viewBox="0 0 122 122" aria-label="Vol. 2">
    <circle cx="61" cy="61" r="57" fill="none" stroke="var(--blue)" stroke-width="4"/>
    <g transform="rotate(-18 61 61)" fill="var(--blue)" font-family="Merriweather Sans, sans-serif" font-weight="800">
      <text x="14" y="80" font-size="26">Vol.</text>
      <text x="68" y="80" font-size="44">2</text>
    </g>
  </svg>
  <h2 class="abs subtitle">HEISS GESCHÜTTELT,&nbsp; NICHT KALT GERÜHRT</h2>

  <div class="abs hero-photo" role="img" aria-label="Foto einer fröhlichen älteren Frau mit türkisfarbenem Schal, Daumen hoch"></div>

  <p class="abs tagline">Mit noch mehr Antworten<br>und Tipps für diese<br>spannende Zeit</p>
  <p class="abs intro">Ein spannendes Tagesseminar über<br>die Wechselbäder der Gefühle, über<br>Hormone, Orientierung, Hilfen und<br>Möglichkeiten. Über die Zeit davor,<br>mittendrin und danach.</p>

  <div class="abs date">23.09.2017</div>
  <div class="abs meta meta-time"><span class="light">Seminar</span> <span class="small">VON</span> 9.00 — 15.00 <span class="small">UHR</span></div>
  <div class="abs meta meta-place"><span class="light">Ort:</span> BILDUNGSHAUS ST. ALWIN, 3912 FELDAU</div>

  <div class="abs band"></div>
  <h3 class="abs band-heading h-change">Über Abschied, Umbruch, Sinnorientierung und Neuanfang.</h3>
  <p class="abs body-col col-left">
    <span>Die Wechseljahre sind keine Krankheit und</span>
    <span>sie kommen nicht über Nacht. Sie sind eine</span>
    <span>Einladung an uns Frauen, uns in den vielfältigen</span>
    <span>Veränderungen, die sich in Körper, Geist und</span>
    <span>Seele vollziehen, neu zu erfahren. Unsere wahre</span>
  </p>
  <p class="abs body-col col-right">
    <span>Schönheit und unser sinnliches Erleben sind von</span>
    <span>äußeren Dingen unabhängig und blühen gerade im</span>
    <span>Älterwerden auf eine neue und besondere Weise</span>
    <span>auf! Das Seminar zeigt auf, in welcher Form uns</span>
    <span class="last">dabei die Hormone sogar unterstützen.</span>
  </p>

  <h3 class="abs band-heading h-questions">Kennen Sie diese Fragen?</h3>
  <ul class="abs questions q-left">
    <li>Wechseljahre, was heisst das für mich?<br>Was passiert gerade mit mir?</li>
    <li>Was möchte ich vom Leben, welche<br>Träume und Wünsche habe ich?</li>
    <li>Was kann ich für mich in dieser Zeit tun?</li>
  </ul>
  <ul class="abs questions q-right">
    <li>Weshalb stelle ich so vieles in Frage und grübele?</li>
    <li>Weshalb kann ich so schlecht<br>einschlafen oder durchschlafen?</li>
    <li>Soll ich Hormone nehmen, was gibt es<br>sonst noch für Möglichkeiten?</li>
  </ul>

  <div class="abs portrait" role="img" aria-label="Porträtfoto der Seminarleiterin"></div>
  <div class="abs brand-mark">Herzwege</div>

  <div class="abs contact">
    <p class="contact-title">Anmeldung unter:</p>
    <p class="contact-line">www.wandelzeit-seminar.ch / info@herzwege-lernen.ch / 078 / 41 26 903</p>
    <p class="contact-name">Mira Tallberg,</p>
    <p class="contact-role">Dipl. Wechseljahresberaterin, Sexualtherapeutin und Mentaltrainerin</p>
    <p class="contact-web">www.Herzwege-lernen.ch</p>
  </div>
  <div class="abs footer-bar"></div>
</div>
</body>
</html>
```